Painting Company Business Card

Brightwell Painting needs a new business card. See attachments for our logo and current card as an example.
We want to utilize the same colors in the logo, and keep all the information that is currently on it. Just need an updated and modern design.
We are open to loosing the Association Logos if it means a better design.
We are also entertaining a spot for a picture of a headshot of the person listed on the card. Head shot can be finished later.

```html
<!DOCTYPE html>
<html lang="en">
<head>
<meta charset="utf-8">
<title>Brightwell Painting – Business Card</title>
<link rel="stylesheet" href="https://fonts.googleapis.com/css2?family=Montserrat:wght@600;700;800&family=Open+Sans:wght@400;600&display=swap">
<style>
  :root {
    --backdrop: #c5cfce;
    --card-white: #ffffff;
    --olive: #566a1c;
    --olive-dark: #3f5213;
    --maroon: #7a0505;
    --magenta: #f03cc8;
    --sky: #5fd0f2;
    --orange: #f7941d;
    --badge: #d8dde3;
    --text-dark: #3a3a3a;
  }
  * { box-sizing: border-box; margin: 0; padding: 0; }
  html, body { width: 1200px; height: 1000px; overflow: hidden; }
  body {
    background: var(--backdrop);
    font-family: "Open Sans", sans-serif;
    position: relative;
  }
  .card {
    position: absolute;
    width: 525px;
    height: 300px;
    border-radius: 18px;
    overflow: hidden;
    background: var(--card-white);
    box-shadow: 0 6px 14px rgba(0,0,0,0.25);
  }
  .card-services { left: 180px; top: 130px; }
  .card-contact { left: 495px; top: 560px; }
  .card-art { position: absolute; inset: 0; width: 100%; height: 100%; }

  .brand {
    position: absolute;
    display: flex;
    align-items: center;
    gap: 8px;
    font-family: "Montserrat", sans-serif;
    font-weight: 800;
    color: var(--olive);
    line-height: 1;
    white-space: nowrap;
  }
  .brand-mark {
    width: 14px; height: 14px;
    background: var(--maroon);
    flex: none;
  }
  .card-services .brand { right: 28px; top: 32px; font-size: 22px; }
  .card-contact .brand { left: 30px; top: 212px; font-size: 22px; }

  .services {
    position: absolute;
    left: 30px; top: 96px;
    color: var(--text-dark);
  }
  .services-title {
    font-family: "Montserrat", sans-serif;
    font-weight: 700;
    font-size: 15px;
    color: var(--olive);
    border-bottom: 2px solid var(--olive);
    display: inline-block;
    padding-bottom: 1px;
    margin-bottom: 3px;
  }
  .services-list { list-style: none; font-size: 16px; line-height: 19px; }
  .services-list li::before { content: "•"; margin-right: 8px; color: var(--text-dark); }

  .person {
    position: absolute;
    left: 300px; top: 22px;
    padding-left: 14px;
    border-left: 4px solid var(--sky);
    color: #fff;
  }
  .person-name { font-family: "Montserrat", sans-serif; font-weight: 700; font-size: 19px; line-height: 1.15; }
  .person-role { font-size: 13px; opacity: 0.95; }

  .contact-list {
    position: absolute;
    left: 345px; top: 84px;
    width: 172px;
    list-style: none;
    color: #fff;
    font-size: 12.5px;
  }
  .contact-list li {
    height: 30px;
    line-height: 30px;
    border-bottom: 1px solid rgba(255,255,255,0.45);
    white-space: nowrap;
  }
  .contact-list li:last-child { border-bottom: none; }
</style>
</head>
<body>

  <section class="card card-services" aria-label="Services side of the card">
    <svg class="card-art" viewBox="0 0 525 300" aria-hidden="true">
      <path d="M525,60 C505,150 470,185 430,215 C480,190 515,150 525,120 Z" fill="var(--orange)"/>
      <path d="M510,70 C490,140 440,190 380,225 C450,195 500,150 520,85 Z" fill="var(--sky)"/>
      <path d="M0,300 L0,268 C150,275 330,250 430,200 C480,170 510,130 525,95 L525,300 Z" fill="var(--olive)"/>
      <path d="M0,300 L0,285 C170,290 360,265 525,170 L525,300 Z" fill="var(--olive-dark)" opacity="0.45"/>
      <path d="M0,248 C110,262 240,250 330,205 C250,262 110,275 0,262 Z" fill="var(--magenta)"/>
      <g fill="var(--badge)">
        <rect x="200" y="210" width="58" height="30" rx="4"/>
        <rect x="268" y="200" width="40" height="42" rx="4"/>
        <rect x="320" y="160" width="34" height="44" rx="5" fill="#b9c8e6"/>
        <rect x="366" y="140" width="52" height="36" rx="4"/>
        <rect x="428" y="118" width="52" height="28" rx="4" fill="#c9d2ec"/>
        <rect x="470" y="82" width="46" height="24" rx="4"/>
      </g>
    </svg>

    <div class="brand"><span class="brand-mark"></span>Brightwell Painting</div>

    <div class="services">
      <h2 class="services-title">OUR SERVICES</h2>
      <ul class="services-list">
        <li>Exterior Painting</li>
        <li>Interior Painting</li>
        <li>Carpentry</li>
        <li>Drywall</li>
      </ul>
    </div>
  </section>

  <section class="card card-contact" aria-label="Contact side of the card">
    <svg class="card-art" viewBox="0 0 525 300" aria-hidden="true">
      <polygon points="0,0 525,0 525,250 0,60" fill="var(--maroon)"/>
      <polygon points="0,60 525,250 525,260 0,70" fill="var(--sky)"/>
      <rect x="305" y="84" width="32" height="90" rx="6" fill="var(--sky)"/>
      <g fill="none" stroke="#fff" stroke-width="1.6" stroke-linecap="round" stroke-linejoin="round">
        <path d="M315,92 c0,6 4,11 10,12 l2,-3 -3,-2 -2,2 c-2,-1 -4,-3 -5,-5 l2,-2 -2,-3 z"/>
        <rect x="312" y="123" width="18" height="12" rx="1"/>
        <path d="M312,123 l9,7 9,-7"/>
        <circle cx="321" cy="159" r="8"/>
        <path d="M313,159 h16 M321,151 c-4,4 -4,12 0,16 M321,151 c4,4 4,12 0,16"/>
      </g>
      <path d="M0,300 L0,270 C40,268 60,278 80,300 Z" fill="var(--orange)"/>
      <path d="M0,265 C45,260 75,275 95,300 L88,300 C70,280 42,268 0,272 Z" fill="var(--sky)"/>
      <path d="M190,300 C300,288 440,278 525,262 L525,300 Z" fill="var(--olive)"/>
      <path d="M230,300 C340,294 450,286 525,276 L525,300 Z" fill="var(--olive-dark)" opacity="0.5"/>
      <path d="M200,278 C300,268 390,255 440,236 C400,265 300,283 200,285 Z" fill="var(--magenta)"/>
    </svg>

    <div class="person">
      <h1 class="person-name">Daniel Harmon</h1>
      <p class="person-role">Quality Manager</p>
    </div>

    <ul class="contact-list">
      <li class="contact-phone">262-555-0147</li>
      <li class="contact-email">D.Harmon@brightwell.com</li>
      <li class="contact-web">BrightwellPainting.com</li>
    </ul>

    <div class="brand"><span class="brand-mark"></span>Brightwell Painting</div>
  </section>

</body>
</html>
```